Meridale Legal Letterhead for Law firm must be modern and use the logo I uploaded.

Hello I want a clean modern professional letterhead for my law firm Meridale Legal. A logo has already been created and all files have been uploaded. The information for the firm can be given through message. Please use the logo that has already been created. Please also use the color scheme of that logo. (blue and white).

Target Market(s)

General Public

Industry/Entity Type

Law Firm

Colors

Designer to choose colors to be used in the design.

Requirements
Must have
• This must be a modern professional letterhead
Nice to have
• My logo that is included in file form
Should not have
• Should not have logo that is not the one I uploaded.

```html
<!DOCTYPE html>
<html lang="en">
<head>
<meta charset="utf-8">
<title>Meridale Legal Letterhead</title>
<link href="https://fonts.googleapis.com/css2?family=Arimo:wght@400&family=Mulish:wght@500;600;700&display=swap" rel="stylesheet">
<style>
  :root{
    --navy:#2d3262;
    --paper:#ffffff;
    --backdrop:#dcdcdc;
    --ink:#55565a;
    --ink-dark:#444548;
  }
  html,body{margin:0;padding:0;width:1189px;height:1200px;overflow:hidden;background:var(--backdrop);}
  .letterhead{
    position:absolute;left:184px;top:20px;width:820px;height:1160px;
    background:var(--paper);overflow:hidden;
    box-shadow:2px 3px 6px rgba(0,0,0,.25);
  }
  .header-wave{position:absolute;left:0;top:0;width:820px;height:182px;display:block;}
  .firm-name{
    position:absolute;left:69px;top:140px;margin:0;
    font-family:"Mulish",sans-serif;font-weight:600;font-size:16px;
    letter-spacing:.32em;color:var(--navy);text-transform:uppercase;
  }
  .contact{
    position:absolute;left:634px;top:39px;margin:0;padding:0;list-style:none;
    font-family:"Arimo",sans-serif;font-size:12.5px;line-height:15.5px;color:#fff;
  }
  .contact li{display:flex;align-items:flex-start;gap:8px;}
  .contact li + li{margin-top:0;}
  .contact .address{margin-bottom:7px;}
  .contact svg{width:10px;height:10px;flex:none;margin-top:3px;fill:#fff;}
  .salutation{
    position:absolute;left:73px;top:350px;margin:0;
    font-family:"Mulish",sans-serif;font-weight:600;font-size:19px;color:var(--ink);
  }
  .body-copy{position:absolute;left:73px;top:408px;width:675px;}
  .body-copy p{
    margin:0 0 14px;font-family:"Arimo",sans-serif;font-size:13px;line-height:17px;color:var(--ink);
  }
  .closing{
    position:absolute;left:73px;top:758px;margin:0;
    font-family:"Mulish",sans-serif;font-weight:700;font-size:10.5px;color:var(--ink-dark);
  }
  .signature{
    position:absolute;left:73px;top:804px;width:135px;height:42px;
    background:linear-gradient(90deg,#e9e9ea,#dadadc);border-radius:3px;
  }
</style>
</head>
<body>
<main class="letterhead">
  <svg class="header-wave" viewBox="0 0 1040 230" preserveAspectRatio="none" aria-hidden="true">
    <path d="M0,0 H1040 V225 C900,238 760,205 600,140 C450,80 250,40 0,95 Z" fill="var(--navy)"/>
    <path d="M0,52 C260,0 470,30 620,85 C790,150 900,200 1040,190" fill="none" stroke="#fff" stroke-width="9"/>
    <path d="M0,98 C250,42 450,80 600,142 C760,205 900,236 1040,226 V240 H0 Z" fill="#fff"/>
    <path d="M155,55 C320,45 470,70 580,112 C470,78 330,58 155,55 Z" fill="var(--navy)"/>
  </svg>

  <p class="firm-name">Meridale Legal</p>

  <ul class="contact">
    <li class="address"><svg viewBox="0 0 10 10"><path d="M5 0a3.6 3.6 0 0 0-3.6 3.6C1.4 6.3 5 10 5 10s3.6-3.7 3.6-6.4A3.6 3.6 0 0 0 5 0zm0 5a1.4 1.4 0 1 1 0-2.8A1.4 1.4 0 0 1 5 5z"/></svg><span>Your address, city<br>state, ZIP 0000</span></li>
    <li><svg viewBox="0 0 10 10"><path d="M2 .5l2 2-1 1.3a6 6 0 0 0 3.2 3.2l1.3-1 2 2-1.3 1.5C4.8 9.5.5 5.2.5 1.8z"/></svg><span>555-014-2100</span></li>
    <li><svg viewBox="0 0 10 10"><path d="M0 2h10v6H0zm1 .8L5 5.6 9 2.8v-.1H1z"/></svg><span>hello@meridalelegal.com</span></li>
    <li><svg viewBox="0 0 10 10"><path d="M5 0a5 5 0 1 0 0 10A5 5 0 0 0 5 0zm0 1.2c.8.8 1.2 2.2 1.3 3.3H3.7c.1-1.1.5-2.5 1.3-3.3zM3.7 5.5h2.6C6.2 6.6 5.8 8 5 8.8 4.2 8 3.8 6.6 3.7 5.5z"/></svg><span>www.meridalelegal.com</span></li>
  </ul>

  <h1 class="salutation">Dear Mr. Smith,</h1>

  <section class="body-copy">
    <p>Lorem ipsum dolor sit amet, consectetuer adipiscing elit, sed diam nonmmy nibh euismod tincidunt ut laor eet dolore magna aliquam erat volutpat. Ut wisi enim ad minim veniam, quis nostrud exerci tationmcorper suscipit lobortis nisl ut aliquip ex ea commodo consequat. Duis autem vel eum iriure dolor in hendrerit in vulputate velit esse molestie consequat, vel illum dolore eu feugiat</p>
    <p>Rorem ipsum dolor sit amet, consectetuer adipiscing elit, sed diam nonmmy nibh euismod tincidunt ut laor eet dolore magna aliquam erat volutpat. Ut wisi enim ad minim veniam, quis nostrud exerci tationmcorper suscipit lobortis nisl ut aliquip ex ea commodo consequat. Duis autem vel eum iriure dolor in hendrerit in vulputate velit esse molest</p>
    <p>Dorem ipsum dolor sit amet, consectetuer adipiscing elit, sed diam nonmmy nibh euismod tincidunt ut laor eet dolore magna aliquam erat volutpat. Ut wisi enim ad minim veniam, quis nostrud exerci tationmcorper suscipit lobortis nisl ut aliquip ex ea commodo consequat. Duis autem vel eum iriure dolor in hendrerit in suscipit lobortis nisl ut aliquip ex ea commodo consequat. Duis autem vel eum iriure dolor in hendrerit in vulputate velit esse molestie consequat, vel illum</p>
    <p>Sorem ipsum dolor sit amet, consectetuer adipiscing elit, sed diam nonmmy nibh euismod tincidunt ut laor eet dolore magna aliquam erat volutpat. Ut wisi enim ad minim veniam, quis nostrud exerci tationmcorper suscipit lobortis nisl ut aliquip ex ea commodo consequat. Duis autem vel eum iriure dolor in</p>
  </section>

  <p class="closing">Sincerely,</p>
  <div class="signature" role="img" aria-label="Handwritten signature of the sender"></div>
</main>
</body>
</html>
```